Design Challege - Simplify a Complex Message

We have a new website design, but one of the pages presents a particular problem.

Our company does ERP implementations. We have developed a proprietary approach to these implementations based on the idea that you must get eight (and only eight) things right. These eight things are listed below, summarized in one or two words each:

1. Value
2. Capability
3. Functionality
4. Data
5. Technology
6. Change Leadership
7. Quality
8. Governance

Each of these eight things can be summarized in a short paragraph, but when you combine all eight summaries with a brief introductory text, the result is a lot of text - so much text that the casual surfer may be overwhelmed by it.

The winning design will find an engaging way to present the information in a way that presents a high-level summary, using icons and one- or two-word descriptions above but revealing more information when clicked.

Our current design for this information, with a paragraph describing the eight elements in a table, is included as an upload in PDF and Microsoft Word formats. We are looking for a creative way to display these eight things, showing the detail only when the user wants to see it.

The website is being built in WordPress, using Elementor as a page builder.

We will implement (code) the page, but the winner will be asked to specify the widget or other add-in if one is required.

The design does not need to include a header or footer, we have those.

Target Market(s)

Business executives working in technology

Industry/Entity Type

Any

Number of Pages Required

1 page

Font styles to use
Sans Serif

Requirements
Must have
• A design for the body of the page, but not the header or footer.
Nice to have
• Unique icons or images appropriate for each of the eight things.
Should not have
• A lot of text on one page

```html
<!DOCTYPE html>
<html lang="en">
<head>
<meta charset="utf-8">
<title>ERP Implementations – Eight Things to Get Right</title>
<link href="https://fonts.googleapis.com/css2?family=Roboto:wght@400;500&display=swap" rel="stylesheet">
<style>
:root{
  --ink:#222;
  --body:#333;
  --accent:#3d8fd6;
  --value-a:#86c63b;--value-b:#a9d93a;
  --capability-a:#3aa6e0;--capability-b:#3a97d8;
  --functionality-a:#3cc69c;--functionality-b:#3dbf92;
  --data-a:#3b86dd;--data-b:#4a7fd9;
  --technology-a:#2c9a93;--technology-b:#35a39c;
  --change-a:#4a69a8;--change-b:#5873ad;
  --quality-a:#34c5dc;--quality-b:#3ccde0;
  --governance-a:#5040a8;--governance-b:#4a38a0;
}
*{box-sizing:border-box;margin:0;padding:0}
html,body{width:1200px;height:2406px;overflow:hidden;background:#fff}
body{font-family:'Roboto',sans-serif;color:var(--body);position:relative}
.page-title{position:absolute;top:56px;width:100%;text-align:center;font-size:41px;font-weight:500;color:var(--ink)}
.page-subtitle{position:absolute;top:117px;width:100%;text-align:center;font-size:21px;color:var(--accent)}
.intro{position:absolute;top:166px;left:130px;width:940px;text-align:center;font-size:15px;line-height:28.5px;color:#333}
.card{position:absolute;background:#fff;box-shadow:0 14px 24px -8px rgba(60,80,120,.16),0 0 10px rgba(60,80,120,.05)}
.card.left{left:112px;width:788px}
.card.right{left:302px;width:786px}
.card-text{position:absolute;font-size:13.5px;line-height:24px;text-align:center;color:#333}
.card.left .card-text{left:215px;width:530px}
.card.right .card-text{left:51px;width:530px}
.card-text ul{list-style:none;text-align:left}
.card-text li::before{content:"• "}
.card-text b{font-weight:500;color:#222}
.learn-more{display:inline-block;margin-top:12px;font-size:13.5px;text-decoration:underline}
.tag{position:absolute;width:206px}
.card.left .tag{left:0}
.card.right .tag{right:0}
.tag svg.shape{position:absolute;left:0;top:0}
.tag-content{position:absolute;top:0;width:146px;height:100%;display:flex;flex-direction:column;align-items:center;justify-content:center;gap:8px;color:#fff;font-size:18.5px;font-weight:500;text-align:center;line-height:24px}
.card.left .tag-content{left:0}
.card.right .tag-content{right:0}
.tag-content svg{stroke:#fff;fill:none;stroke-width:1.6;stroke-linecap:round;stroke-linejoin:round}
</style>
</head>
<body>
<h1 class="page-title">ERP Implementations</h1>
<h2 class="page-subtitle">Eight Things to Get Right</h2>
<p class="intro">Like the roots and branches of a tree, there are many considerations in an ERP implementation. Focus too much on &nbsp;the minor details, and you can lose sight of the tree.<br>In an ERP implementation, you must get eight major things right to be successful. Ignore any of them, and your &nbsp;implementation will fail. Get them right, and you will likely succeed.</p>

<!-- Value -->
<section class="card left" style="top:332px;height:173px">
  <div class="tag" style="top:30px;height:136px">
    <svg class="shape" width="206" height="136"><defs><linearGradient id="g-value" x1="0" x2="1"><stop offset="0" stop-color="var(--value-a)"/><stop offset="1" stop-color="var(--value-b)"/></linearGradient></defs><path d="M12 0H118Q128 0 134 9L206 136H12Q0 136 0 124V12Q0 0 12 0Z" fill="url(#g-value)"/></svg>
    <div class="tag-content"><svg width="56" height="52" viewBox="0 0 56 52"><path d="M14 16h28l8 9-22 22L6 25z"/><path d="M6 25h44M20 16l-4 9 12 22 12-22-4-9M28 16v0"/><path d="M28 2v6M12 6l3 4M44 6l-3 4M2 25h2M52 25h2"/></svg>Value</div>
  </div>
  <div class="card-text" style="top:30px">The project must provide value that significantly exceeds potential project costs and should be aligned with the company's strategy. Its value and strategic alignment must be part of a vision shared by the company's leadership. Value from the project must be delivered in a way that respects resource constraints.<br><a class="learn-more" style="color:var(--value-a)">Learn More</a></div>
</section>

<!-- Capability -->
<section class="card right" style="top:586px;height:203px">
  <div class="tag" style="top:26px;height:168px">
    <svg class="shape" width="206" height="168"><defs><linearGradient id="g-cap" x1="0" x2="1"><stop offset="0" stop-color="var(--capability-a)"/><stop offset="1" stop-color="var(--capability-b)"/></linearGradient></defs><path d="M88 0H194Q206 0 206 12V156Q206 168 194 168H0L76 9Q82 0 88 0Z" fill="url(#g-cap)"/></svg>
    <div class="tag-content"><svg width="60" height="76" viewBox="0 0 60 76"><path d="M22 74V60Q6 54 4 36Q4 8 30 4Q54 4 56 30Q56 46 48 52V74"/><circle cx="30" cy="22" r="7"/><circle cx="38" cy="40" r="7"/><circle cx="18" cy="38" r="5"/><path d="M30 11v-3M30 36v-3M19 22h-3M44 22h-3M38 29v-3M38 54v-3M27 40h-3M52 40h-3"/></svg>Capability</div>
  </div>
  <div class="card-text" style="top:30px">The company and the implementation team must be capable of implementing the project on their own or with help. The project must have the following:
    <ul><li><b>Resources required</b>, including people, time, and budget.</li><li><b>Processes required</b>, usually delivered through a comprehensive methodology.</li><li><b>Prioritization required</b> because an ERP project will need the commitment of the entire company.</li></ul>
    <a class="learn-more" style="color:var(--capability-a)">Learn More</a></div>
</section>

<!-- Functionality -->
<section class="card left" style="top:870px;height:170px">
  <div class="tag" style="top:30px;height:132px">
    <svg class="shape" width="206" height="132"><defs><linearGradient id="g-fun" x1="0" x2="1"><stop offset="0" stop-color="var(--functionality-a)"/><stop offset="1" stop-color="var(--functionality-b)"/></linearGradient></defs><path d="M12 0H118Q128 0 134 9L206 132H12Q0 132 0 120V12Q0 0 12 0Z" fill="url(#g-fun)"/></svg>
    <div class="tag-content"><svg width="56" height="52" viewBox="0 0 56 52"><circle cx="26" cy="24" r="12"/><circle cx="26" cy="24" r="7"/><circle cx="26" cy="24" r="3"/><circle cx="8" cy="8" r="5"/><path d="M6 8l2 2 3-4"/><circle cx="44" cy="44" r="5"/><path d="M42 44l2 2 3-4"/><path d="M40 14V8M44 14V4M48 14V6M4 36h10v12H4zM7 40h4M20 38v8h10v-8"/></svg>Functionality</div>
  </div>
  <div class="card-text" style="top:26px">An ERP project must support required business processes, both now and in the future. A systematic review of all business processes and how they will be supported, either by the system or otherwise, is crucial.<br><a class="learn-more" style="color:var(--functionality-a)">Learn More</a></div>
</section>

<!-- Data -->
<section class="card right" style="top:1116px;height:180px">
  <div class="tag" style="top:28px;height:144px">
    <svg class="shape" width="206" height="144"><defs><linearGradient id="g-data" x1="0" x2="1"><stop offset="0" stop-color="var(--data-a)"/><stop offset="1" stop-color="var(--data-b)"/></linearGradient></defs><path d="M88 0H194Q206 0 206 12V132Q206 144 194 144H0L76 9Q82 0 88 0Z" fill="url(#g-data)"/></svg>
    <div class="tag-content"><svg width="56" height="52" viewBox="0 0 56 52"><path d="M4 50V34h6v16M14 50V26h6v24M24 50V30h6v20M34 50V20h6v30M44 50V10h6v40M2 50h52"/><path d="M6 26l10-10 10 6 14-12 8-6"/><circle cx="48" cy="4" r="2"/></svg>Data</div>
  </div>
  <div class="card-text" style="top:34px">ERP systems are data-hungry creatures. Please be careful before assuming that because so much data goes into them, an equal amount of insight will emerge. Getting data right means considering data architecture, migration, integration, governance, and, perhaps most importantly, access<br><a class="learn-more" style="color:var(--data-a)">Learn More</a></div>
</section>

<!-- Technology -->
<section class="card left" style="top:1368px;height:171px">
  <div class="tag" style="top:28px;height:135px">
    <svg class="shape" width="206" height="135"><defs><linearGradient id="g-tech" x1="0" x2="1"><stop offset="0" stop-color="var(--technology-a)"/><stop offset="1" stop-color="var(--technology-b)"/></linearGradient></defs><path d="M12 0H118Q128 0 134 9L206 135H12Q0 135 0 123V12Q0 0 12 0Z" fill="url(#g-tech)"/></svg>
    <div class="tag-content"><svg width="60" height="56" viewBox="0 0 60 56"><path d="M30 6a22 22 0 1 0 0 44M30 14a14 14 0 1 0 0 28"/><path d="M8 28H2M12 12L8 8M12 44l-4 4M30 6V2M30 54v-4"/><path d="M30 20h14l4-6h6M30 28h22M30 36h14l4 6h6"/><circle cx="56" cy="14" r="2"/><circle cx="56" cy="42" r="2"/></svg>Technology</div>
  </div>
  <div class="card-text" style="top:26px">What is the platform for the system? Is it offered by a vendor that will be around for as long as your system? Will it integrate with your other systems? Are resources available to support it? Can you change it without painting yourself into a corner? Will your technology scale as you grow?<br><a class="learn-more" style="color:var(--technology-a)">Learn More</a></div>
</section>

<!-- Change Leadership -->
<section class="card right" style="top:1620px;height:176px">
  <div class="tag" style="top:28px;height:144px">
    <svg class="shape" width="206" height="144"><defs><linearGradient id="g-change" x1="0" x2="1"><stop offset="0" stop-color="var(--change-a)"/><stop offset="1" stop-color="var(--change-b)"/></linearGradient></defs><path d="M88 0H194Q206 0 206 12V132Q206 144 194 144H0L76 9Q82 0 88 0Z" fill="url(#g-change)"/></svg>
    <div class="tag-content"><svg width="50" height="56" viewBox="0 0 50 56"><path d="M16 54V42l-4-6V24q0-4 4-4t4 4v-2q0-4 4-4t4 4v2q0-4 4-4t4 4v14l-4 6v12"/><path d="M20 24v8M28 24v8M14 42h20M24 2v6M12 6l3 5M36 6l-3 5M42 16h4"/></svg>Change<br>Leadership</div>
  </div>
  <div class="card-text" style="top:34px">Change leadership (often called change management) considers the human side of an ERP implementation. Change is hard, even if it's a good change. Training is an important element of change leadership. But beyond training, consideration must be given to the people using the system.<br><a class="learn-more" style="color:var(--change-a)">Learn More</a></div>
</section>

<!-- Quality -->
<section class="card left" style="top:1882px;height:171px">
  <div class="tag" style="top:28px;height:135px">
    <svg class="shape" width="206" height="135"><defs><linearGradient id="g-qual" x1="0" x2="1"><stop offset="0" stop-color="var(--quality-a)"/><stop offset="1" stop-color="var(--quality-b)"/></linearGradient></defs><path d="M12 0H118Q128 0 134 9L206 135H12Q0 135 0 123V12Q0 0 12 0Z" fill="url(#g-qual)"/></svg>
    <div class="tag-content"><svg width="50" height="50" viewBox="0 0 50 50"><path d="M25 3l5 4 6-1 3 6 6 3-1 6 4 5-4 5 1 6-6 3-3 6-6-1-5 4-5-4-6 1-3-6-6-3 1-6-4-5 4-5-1-6 6-3 3-6 6 1z"/><circle cx="25" cy="25" r="13"/><path d="M19 25l4 4 8-8"/></svg>Quality</div>
  </div>
  <div class="card-text" style="top:26px">Quality is multi-dimensional, and it's more than a measurement; it's a perception. An ERP needs to be reliable. But poor performance or poor user experience are often root causes of implementation failure. Take an approach to quality that starts with perceptions and considers all aspects of quality.<br><a class="learn-more" style="color:var(--quality-a)">Learn More</a></div>
</section>

<!-- Governance -->
<section class="card right" style="top:2134px;height:178px">
  <div class="tag" style="top:28px;height:144px">
    <svg class="shape" width="206" height="144"><defs><linearGradient id="g-gov" x1="0" x2="1"><stop offset="0" stop-color="var(--governance-a)"/><stop offset="1" stop-color="var(--governance-b)"/></linearGradient></defs><path d="M88 0H194Q206 0 206 12V132Q206 144 194 144H0L76 9Q82 0 88 0Z" fill="url(#g-gov)"/></svg>
    <div class="tag-content"><svg width="64" height="56" viewBox="0 0 64 56"><circle cx="32" cy="26" r="20"/><circle cx="32" cy="14" r="5"/><path d="M24 28q0-7 8-7t8 7"/><path d="M4 40l10-6 10 4 8 6-4 4-8-4M60 40l-10-6-12 6-8 6 4 4 10-6M20 48l4 4M24 44l6 6"/></svg>Governance</div>
  </div>
  <div class="card-text" style="top:32px">ERP projects require both management and leadership. Planning, changing plans, communication, decision making, and guidance are critical aspects of management. But without the leadership qualities of motivating a team, setting clear goals, and using influence to reach goals, even well-managed projects can fail.<br><a class="learn-more" style="color:var(--governance-a)">Learn More</a></div>
</section>
</body>
</html>
```